Werbeanzeige/Werbemittel im BWV-Magazin (Printausgabe)
Zielgruppe
VELMARIXA ist ein mehrköpfiges Team an Spezialisten für Online- und Performance-Marketing sowie Webgestaltung. Unser Team arbeitet motiviert, kreativ und leistungsorientiert. Wir finden Online-Marketing-Lösungen, die Ihre Unternehmenstrategie konsequent unterstützen. Kosteneffizient und zielorientiert.
Wir sind Experten im Bereich Suchmaschinenoptimierung (SEO), Suchmaschinenmarketing (SEA), Social Media und Affiliate Marketing.
Unser Leistungsspektrum umfasst sowohl die persönliche Beratung, als auch die Konzeptionierung von Online-Kampagnen und die Umsetzung von Maßnahmen für erfolgreiches eCommerce. Salesorientierte Webvermarktung, gezielte Kundengewinnung und langfristige Kundenbindung verstehen wir als nachhaltiges Konzept zur Performancesteigerung.
Aufgabenstellung
In der September Ausgabe der BWV-Zeitschrift (Bund- und Wirtschaftsverein) erscheint eine Werbeanzeige von unserer Agentur VELMARIXA.
Das von uns gebuchte Format (1/3 Seite) können wir in zwei unterschiedlichen Größen erstellen:
1) Im Satzspiegel: 188 mm breit/ 84 mm hoch
2) Im Anschnitt : 210 mm breit/ 90 mm hoch + 3mm Beschnitt an drei Seiten
Im Anhang findet ihr auch einige Beispiele anderer Unternehmen die ähnliche Werbung (in Bezug auf das Format) in der Vergangenheit geschalten haben.
Unsere Zielsetzung ist:
Wir möchten klein-/ mittelständische Unternehmen aus dem gesamten Ruhrgebiet bevorzugt von unserer: fachlichen KOMPETENEZ, SERIÖSITÄT, FLEXIBILITÄT & TRANSPARENZ überzeugen und als Neukunden in den Bereichen: Suchmaschinenmarketing (KlickPlan), Suchmaschinenoptimierung (SEO) & Webentwicklung (Webseiten, Shops) gewinnen.
Bitte schaut euch unsere Webseite: www.velmarixa-web.com an.
PS: Wir sind Quorvan Zertifiziert!
Bzgl. Wording habt ihr freie Hand. (als Beispiel: "Gefunden werden wo es wichtig ist")
Wir freuen uns auf Eure Vorschläge!

```html
<!DOCTYPE html>
<html lang="de">
<head>
<meta charset="utf-8">
<title>VELMARIXA – Anzeige</title>
<link rel="stylesheet" href="https://fonts.googleapis.com/css2?family=Open+Sans:wght@400;600&display=swap">
<style>
  :root {
    --page-bg: #dcdcdc;
    --ad-bg: #ffffff;
    --brand-blue: #1f7bc0;
    --brand-green: #7ba82c;
    --brand-grey: #55595c;
    --footer-bg: #e6e6e6;
    --button-bg: #e8e8e8;
    --button-border: #8a8a8a;
    --button-text: #9a9a9a;
    --field-border: #9a9a9a;
    --text-dark: #1a1a1a;
  }
  * { margin: 0; padding: 0; box-sizing: border-box; }
  html, body {
    width: 1200px; height: 675px; overflow: hidden;
    background: var(--page-bg);
    font-family: "Open Sans", sans-serif;
  }
  .ad {
    position: absolute; left: 26px; top: 92px;
    width: 1147px; height: 489px;
    background: var(--ad-bg);
    border: 2px solid var(--brand-blue);
    overflow: hidden;
  }
  .brand {
    position: absolute; left: 0; right: 0; top: 30px;
    text-align: center;
  }
  .brand-name {
    display: block;
    font-size: 58px; font-weight: 600; line-height: 1;
    letter-spacing: 6px;
    color: var(--brand-blue);
    margin-left: 6px;
  }
  .brand-tagline {
    display: block; margin-top: 8px;
    font-size: 26px; font-weight: 600; line-height: 1;
    letter-spacing: 5px;
    color: var(--brand-grey);
  }
  .search-field {
    position: absolute; left: 113px; top: 164px;
    width: 855px; height: 55px;
    border: 2px solid var(--field-border);
    box-shadow: 0 3px 4px rgba(0,0,0,0.25);
    display: flex; align-items: center; justify-content: center;
    font-size: 22.5px; font-weight: 600;
    color: var(--brand-green);
  }
  .search-button {
    position: absolute; left: 977px; top: 164px;
    width: 72px; height: 55px;
    background: var(--brand-blue);
    box-shadow: 0 3px 4px rgba(0,0,0,0.25);
  }
  .search-button svg { position: absolute; left: 16px; top: 10px; }
  .action {
    position: absolute; top: 247px;
    width: 222px; height: 41px;
    background: var(--button-bg);
    border: 2px solid var(--button-border);
    border-radius: 4px;
    box-shadow: 0 5px 6px rgba(0,0,0,0.35);
    display: flex; align-items: center; justify-content: center;
    font-size: 22px; color: var(--button-text);
  }
  .action-search { left: 341px; }
  .action-optimize { left: 580px; }
  .footer {
    position: absolute; left: 0; right: 0; bottom: 0;
    height: 104px;
    background: var(--footer-bg);
    font-size: 19px; line-height: 21px;
    color: var(--text-dark);
  }
  .footer-col { position: absolute; top: 8px; }
  .footer-col h2 { font-size: 19px; font-weight: 400; line-height: 24px; margin-bottom: 18px; }
  .col-contact { left: 63px; }
  .col-services { left: 0; right: 0; text-align: center; padding-left: 24px; }
  .col-address { right: 63px; text-align: right; }
  .contact-row span { display: inline-block; width: 79px; }
</style>
</head>
<body>
  <div class="ad">
    <div class="brand">
      <span class="brand-name">VELMARIXA</span>
      <span class="brand-tagline">ONLINE MEDIA AGENCY</span>
    </div>

    <div class="search-field">Damit Sie nicht verschwinden, lassen Sie sich besser finden.</div>
    <div class="search-button">
      <svg width="40" height="36" viewBox="0 0 40 36" aria-hidden="true">
        <circle cx="14" cy="14" r="11" fill="none" stroke="#fff" stroke-width="2.5"/>
        <line x1="22" y1="22" x2="35" y2="32" stroke="#fff" stroke-width="2.5" stroke-linecap="round"/>
      </svg>
    </div>

    <div class="action action-search">Quorvan-Suche</div>
    <div class="action action-optimize">Optimiert!</div>

    <div class="footer">
      <div class="footer-col col-contact">
        <h2>Kontakt</h2>
        <div class="contact-row"><span>Telefon</span>0211 - 4870 3310</div>
        <div class="contact-row"><span>Fax</span>0211 - 4870 3319</div>
      </div>
      <div class="footer-col col-services">
        <h2>Leistungen</h2>
        <div>SEO·SEA·Lokal Affiliate Marketing</div>
        <div>Social Media·Consulting</div>
      </div>
      <div class="footer-col col-address">
        <h2>Anschrift</h2>
        <div>Lindenhofer Str. 16</div>
        <div>D-40479 Düsseldorf</div>
      </div>
    </div>
  </div>
</body>
</html>
```